Digital Mapping company needs a Proposal Cover Page template (Not Cover Letter).

We are looking for a new design of our proposal's front page. Sales people at Brindle Survey will use this new cover page when bidding for jobs, there will be Brindle Survey elements that will be set in stone but the potential client information will need to be adaptable/customizable (for example, we currently upload client logos to the home page of our proposals). I attach what we currently have.
Similar look and feel as our tradeshow booth pull up banners and website (www.brindlesurvey.example) (images of these are also attached). We would like to see designs that use similar colours: green/blue/teal/yellow/orange/red.

We have clients all over the world. We own state of the art mapping equipment (LiDAR). LiDAR and digital photography are acquired with our own Halvern 314 and other aircraft. The final proposal design should be recognizable and communicate: an experienced company, high quality, and state of the art mapping technology delivered worldwide.

Target Market(s)

Our clients are global and range from small business to large corporations. We have clients associated with Mining, Forestry, Engineering, Ecological and First Nations sectors (usually hired by Geologists & Engineers)

Industry/Entity Type

Technical Service

Font styles to use
Serif

Colors

Designer to choose colors to be used in the design.

Requirements
Must have
• Here are the basic items we would like to see on the cover page of our proposal:
• Our Company Name - Brindle Survey Ltd.
• Our Company Logo - attached
• Our Company contact information [customizable field as we have a few locations]
• Proposal service [customizable field to add]
• Proposal project name and location [customizable field to add]
• Proposal Job number [customizable field to add]
• Recipient company or individual and their logo [customizable field’s to add these]
• Date created [auto date]
• Subdued information/less focus on Brindle Survey’s name and contact information and a greater focus on the client and their project. Well chosen imagery will tie Brindle Survey’s services to the client’s needs without the client thinking about it. Good use of white space as well.
Nice to have
• Similar look and feel as our tradeshow booth pull up banners and website (images of these are attached). We would like to see designs that use similar colours: green/yellow/red/blue/teal.
Should not have
• Something that doesn't match or fit with our logo/website/pull up tradeshow banners that are attached. Something that doesn't include all the elements in our must have list.

```html
<!DOCTYPE html>
<html lang="en">
<head>
<meta charset="utf-8">
<title>Brindle Survey – Proposal Cover</title>
<link rel="stylesheet" href="https://fonts.googleapis.com/css2?family=Noto+Serif:wght@400;600;700;800&display=swap">
<style>
  :root {
    --brand-blue: #2f96c0;
    --brand-blue-dark: #1f7fa8;
    --ink: #2b2b2b;
    --muted: #5a5a5a;
    --paper: #f4f4f4;
    --sky: #5c6577;
    --terrain-red: #c4471e;
    --terrain-amber: #d89a1c;
    --terrain-green: #7dbd2c;
  }
  * { box-sizing: border-box; margin: 0; padding: 0; }
  html, body { width: 1067px; height: 1200px; overflow: hidden; }
  body { background: var(--paper); font-family: "Noto Serif", serif; color: var(--ink); }

  .cover { position: relative; width: 1067px; height: 1200px; background: var(--paper); overflow: hidden; }

  .cover-header { position: absolute; top: 0; left: 0; right: 0; height: 168px; }
  .brand { position: absolute; left: 70px; top: 50px; }
  .brand-mark { display: flex; align-items: center; gap: 14px; }
  .brand-dot { width: 40px; height: 40px; border-radius: 50%; background: var(--brand-blue); flex: none; }
  .brand-name { font-size: 30px; font-weight: 800; color: #1c1c1c; letter-spacing: 0.5px; text-transform: uppercase; line-height: 1; }
  .brand-legal { margin-top: 12px; font-size: 20px; font-weight: 700; color: var(--brand-blue); }

  .header-divider { position: absolute; left: 640px; top: 48px; width: 2px; height: 84px; background: var(--brand-blue); }
  .contact { position: absolute; left: 664px; top: 50px; font-size: 12.5px; line-height: 1.6; color: var(--brand-blue); font-style: normal; white-space: nowrap; }

  .band { position: absolute; left: 0; right: 0; background: var(--brand-blue); }
  .band-top { top: 168px; height: 12px; }
  .band-under-image { top: 606px; height: 14px; }
  .band-footer-thin { top: 1080px; height: 16px; }
  .band-footer { top: 1150px; height: 30px; background: var(--brand-blue-dark); }

  .terrain {
    position: absolute; left: 0; right: 0; top: 180px; height: 426px;
    background: linear-gradient(180deg, var(--sky) 0%, var(--sky) 10%, var(--terrain-red) 24%, #cf6a1d 40%, var(--terrain-amber) 62%, #a9b925 82%, var(--terrain-green) 100%);
  }

  .proposal { position: absolute; left: 80px; top: 660px; right: 80px; }
  .client-logo-field { width: 96px; height: 96px; background: var(--brand-blue); }
  .proposal-title { margin-top: 38px; margin-left: 14px; font-size: 33px; font-weight: 700; line-height: 1.32; text-transform: uppercase; color: var(--ink); }
  .proposal-job { margin-top: 12px; margin-left: 24px; font-size: 29px; font-weight: 600; text-transform: uppercase; color: var(--ink); }
  .proposal-date { margin-top: 10px; margin-left: 24px; font-size: 17px; font-weight: 400; color: var(--muted); }
</style>
</head>
<body>
  <main class="cover">
    <header class="cover-header">
      <div class="brand">
        <div class="brand-mark">
          <span class="brand-dot"></span>
          <span class="brand-name">Brindle Survey</span>
        </div>
        <div class="brand-legal">Brindle Survey Ltd.</div>
      </div>
      <span class="header-divider"></span>
      <address class="contact">
        [Brindle Survey Ltd.<br>
        118-4400 Harbourline Rd.<br>
        Port Alder BC, V0X 2K1, Canada]<br>
        O. +1(555) 010-0199 | info@brindlesurvey.example
      </address>
    </header>

    <div class="band band-top"></div>
    <div class="terrain" role="img" aria-label="LiDAR elevation hillshade of a mountain range, coloured red at the peaks through yellow to green in the valleys"></div>
    <div class="band band-under-image"></div>

    <section class="proposal">
      <div class="client-logo-field" role="img" aria-label="Placeholder for the recipient company logo"></div>
      <h1 class="proposal-title">Proposal to [Service we are<br>providing] in [Project location]<br>for [Company name].</h1>
      <p class="proposal-job">[Job number]</p>
      <p class="proposal-date">[Date created]</p>
    </section>

    <div class="band band-footer-thin"></div>
    <div class="band band-footer"></div>
  </main>
</body>
</html>
```